PowerPoint Slide desk with a Rocketship theme

We are a company that is going through a lot of growth. We internally refer to it as being on a rocketship. Looking for a PowerPoint deck to use with my internal team. I would like it to be fun and cartoonish. The main theme is spaceships/rockets and going on a mission. We will be using this as a way to describe the mission of the company and what the goals of the company are. There should be a title page that can be reused for each team meeting held with a space for a title and date. There should be pages for lots of text. The text must be easy to read on a TV. There should be slides for photos and graphs.

I have included an image of a rocket and a space background. I have included another rocket for example of the type of drawing and look we are looking for. I have also included our company logo.

The rocketship should have the round Signal Forge logo on it. You can have fun and include some alien figures and spacemen.

Target Market(s)

This is for our internal employees. We are and IT company

Industry/Entity Type

Managed IT Services

Font styles to use
Sans Serif

Colors
0054AA
0677BA
7BADD7
CADEEF
E8F1F8

Requirements
Must have
• see images attached for examples of what we are looking for.

```html
<!DOCTYPE html>
<html lang="en">
<head>
<meta charset="utf-8">
<title>Signal Forge – Team Deck</title>
<link rel="stylesheet" href="https://fonts.googleapis.com/css2?family=Fredoka:wght@500;600&family=Poppins:wght@400;500;600&display=swap">
<style>
:root{
  --page:#0d1230;
  --space-deep:#120c3a;
  --space-mid:#2a1b6e;
  --space-glow:#4b2a9a;
  --blue-dark:#0054AA;
  --blue:#0677BA;
  --blue-light:#7BADD7;
  --blue-pale:#CADEEF;
  --blue-ice:#E8F1F8;
  --white:#ffffff;
  --violet:#8a5cf0;
  --card:#0b1e4a;
}
*{margin:0;padding:0;box-sizing:border-box}
html,body{width:1200px;height:4144px;overflow:hidden;background:var(--page)}
body{font-family:"Poppins",sans-serif;color:var(--white)}
.deck{position:relative;width:1200px;height:4144px;padding-top:24px}
.slide{position:relative;width:1072px;height:603px;margin:0 auto 95px;overflow:hidden;
  background:radial-gradient(ellipse at 65% 30%,var(--space-glow) 0%,var(--space-mid) 35%,var(--space-deep) 80%);
  box-shadow:0 10px 40px rgba(0,0,0,.5)}
.slide::before{content:"";position:absolute;inset:0;
  background-image:radial-gradient(1.5px 1.5px at 10% 20%,#fff 50%,transparent),radial-gradient(1px 1px at 30% 70%,#fff 50%,transparent),
  radial-gradient(1.5px 1.5px at 55% 15%,#fff 50%,transparent),radial-gradient(1px 1px at 80% 60%,#fff 50%,transparent),
  radial-gradient(1px 1px at 90% 25%,#fff 50%,transparent),radial-gradient(1.5px 1.5px at 45% 85%,#fff 50%,transparent),
  radial-gradient(1px 1px at 20% 45%,#fff 50%,transparent),radial-gradient(1px 1px at 70% 40%,#fff 50%,transparent);opacity:.8}
.brand{position:absolute;top:22px;right:28px;display:flex;align-items:center;gap:10px;z-index:5}
.brand-dot{width:34px;height:34px;border-radius:50%;background:var(--white)}
.brand-name{font-family:"Fredoka",sans-serif;font-weight:500;font-size:22px;color:var(--white);line-height:1}
.planet-surface{position:absolute;left:-10%;width:120%;height:260px;bottom:-150px;border-radius:50% 50% 0 0;
  background:linear-gradient(180deg,#3fb8e8 0%,#1b6fc4 25%,#3a2f9a 60%,#1a1450 100%)}
.art{position:absolute;background:linear-gradient(160deg,var(--blue-light),var(--violet));border-radius:24px}
.h-title{font-family:"Fredoka",sans-serif;font-weight:600}
.slide-heading{font-family:"Fredoka",sans-serif;font-weight:600;font-size:44px;text-align:center}
.body-text{font-size:12.5px;line-height:1.6;color:var(--blue-ice)}

/* title slide */
.title-block{position:absolute;left:400px;top:110px}
.title-block h1{font-size:76px;line-height:1.05;letter-spacing:1px}
.title-date{font-size:20px;margin-top:14px;color:var(--blue-pale)}
.rocket{left:60px;top:40px;width:170px;height:300px;border-radius:80px 80px 30px 30px;transform:rotate(20deg)}
.moon{position:absolute;left:735px;top:120px;width:22px;height:22px;border-radius:50%;background:#2a2550}

/* mission */
.mission-photo{position:absolute;left:-30px;top:70px;width:440px;height:440px;border-radius:50%;
  background:linear-gradient(135deg,#7a6a8a,#3a3b5a);border:6px solid var(--blue-dark)}
.mission-badge{position:absolute;left:370px;top:70px;width:110px;height:110px;border-radius:50%;background:var(--blue-dark);border:6px solid var(--white)}
.mission-astro{left:320px;top:380px;width:100px;height:120px;border-radius:50px}
.mission-copy{position:absolute;left:585px;top:100px;width:420px}
.mission-copy h2{font-size:44px;margin-bottom:14px}
.check-list{list-style:none;margin-top:16px}
.check-list li{display:flex;gap:10px;margin-bottom:10px}
.check-list svg{flex:0 0 16px;margin-top:3px}

/* about */
.about-copy{position:absolute;left:140px;top:100px;width:792px;text-align:center}
.about-copy .slide-heading{margin-bottom:22px}
.about-copy p{margin-bottom:22px}
.ufo{left:30px;top:30px;width:120px;height:70px;border-radius:60px}
.about-astro{left:940px;top:450px;width:100px;height:120px;border-radius:50px}

/* services */
.services-heading{position:absolute;top:95px;width:100%}
.services-row{position:absolute;top:200px;left:90px;display:flex;gap:52px}
.service{position:relative;width:262px;height:262px;border-radius:50%;overflow:hidden;
  background:linear-gradient(150deg,#8a8a9a,#3a3e60);border:5px solid var(--blue-dark)}
.service-label{position:absolute;bottom:0;left:0;right:0;height:90px;background:rgba(10,16,50,.85);text-align:center;padding-top:16px}
.service-label strong{font-family:"Fredoka",sans-serif;font-size:22px;font-weight:500;display:block}
.service-label span{font-size:11px;color:var(--blue-pale)}
.small-rocket{left:40px;top:40px;width:70px;height:40px;border-radius:20px;transform:rotate(-30deg)}
.alien{left:930px;top:420px;width:110px;height:150px;border-radius:55px;background:linear-gradient(160deg,#7be0f0,#3a6ad0)}

/* charts */
.charts-intro{position:absolute;left:40px;top:78px;width:860px}
.charts-intro h2{font-size:48px;text-align:left;margin-bottom:6px}
.chart{position:absolute;left:30px;top:190px}
.chart-cards{position:absolute;left:650px;top:190px;width:390px}
.chart-card{background:var(--card);border-left:6px solid var(--blue-light);padding:12px 16px;margin-bottom:14px;border-radius:4px}
.chart-card h3{font-family:"Fredoka",sans-serif;font-weight:500;font-size:24px;margin-bottom:4px}
.chart-card p{font-size:11px;line-height:1.5;color:var(--blue-pale)}

/* goals */
.goals-astro{left:40px;top:80px;width:380px;height:480px;border-radius:190px 190px 60px 60px;background:linear-gradient(160deg,var(--blue-ice),var(--blue-light))}
.goals-copy{position:absolute;left:500px;top:100px;width:520px}
.goals-copy .slide-heading{text-align:left;margin-bottom:20px}
.goals-copy p{margin-bottom:20px}
</style>
</head>
<body>
<main class="deck">

  <section class="slide slide-title">
    <div class="brand"><span class="brand-dot"></span><span class="brand-name">Signal Forge</span></div>
    <div class="art rocket" role="img" aria-label="Cartoon rocket illustration lifting off"></div>
    <span class="moon"></span>
    <div class="title-block">
      <h1 class="h-title">Welcome To<br>Signal Forge</h1>
      <p class="title-date">April 24 2023</p>
    </div>
    <div class="planet-surface" role="img" aria-label="Cartoon planet surface with craters"></div>
  </section>

  <section class="slide slide-mission">
    <div class="brand"><span class="brand-dot"></span><span class="brand-name">Signal Forge</span></div>
    <div class="mission-photo" role="img" aria-label="Photo of team members working together at a computer"></div>
    <div class="mission-badge"></div>
    <div class="art mission-astro" role="img" aria-label="Small cartoon astronaut riding a rocket"></div>
    <div class="mission-copy">
      <h2 class="h-title">Our Mission</h2>
      <p class="body-text">Lorem ipsum dolor sit amet, consectetur adipiscing elit, sed do eiusmod tempor incididunt ut labore et dolore magna aliqua. Quis ipsum suspendisse ultrices gravida. Risus commodo viverra maecenas accumsan lacus vel facilisis.</p>
      <ul class="check-list body-text">
        <li><svg width="16" height="16" viewBox="0 0 16 16"><rect x="1" y="1" width="14" height="14" rx="3" fill="#0677BA"/><path d="M4 8l3 3 5-6" stroke="#fff" stroke-width="2" fill="none"/></svg>Lorem ipsum dolor sit amet, consectetur adipiscing elit, sed do eiusmod tempor incididunt ut labore et dolore magna aliqua. Quis ipsum suspendisse ultrices gravida.</li>
        <li><svg width="16" height="16" viewBox="0 0 16 16"><rect x="1" y="1" width="14" height="14" rx="3" fill="#0677BA"/><path d="M4 8l3 3 5-6" stroke="#fff" stroke-width="2" fill="none"/></svg>Lorem ipsum dolor sit amet, consectetur adipiscing elit, sed do eiusmod tempor incididunt ut labore et dolore magna aliqua. Risus commodo viverra.</li>
        <li><svg width="16" height="16" viewBox="0 0 16 16"><rect x="1" y="1" width="14" height="14" rx="3" fill="#0677BA"/><path d="M4 8l3 3 5-6" stroke="#fff" stroke-width="2" fill="none"/></svg>Lorem ipsum dolor sit amet, consectetur adipiscing elit.</li>
        <li><svg width="16" height="16" viewBox="0 0 16 16"><rect x="1" y="1" width="14" height="14" rx="3" fill="#0677BA"/><path d="M4 8l3 3 5-6" stroke="#fff" stroke-width="2" fill="none"/></svg>Lorem ipsum dolor sit amet, consectetur adipiscing elit, sed do.</li>
      </ul>
    </div>
  </section>

  <section class="slide slide-about">
    <div class="brand"><span class="brand-dot"></span><span class="brand-name">Signal Forge</span></div>
    <div class="art ufo" role="img" aria-label="Cartoon flying saucer"></div>
    <div class="about-copy body-text">
      <h2 class="slide-heading">About Us</h2>
      <p>Lorem ipsum dolor sit amet, consectetur adipiscing elit, sed do eiusmod tempor incididunt ut labore et dolore magna aliqua. Quis ipsum suspendisse ultrices gravida. Risus commodo viverra maecenas accumsan lacus vel facilisis.</p>
      <p>Lorem ipsum dolor sit amet, consectetur adipiscing elit, sed do eiusmod tempor incididunt ut labore et dolore magna aliqua. Quis ipsum suspendisse ultrices gravida. Risus commodo viverra maecenas accumsan lacus vel facilisis.</p>
      <p>Lorem ipsum dolor sit amet, consectetur adipiscing elit, sed do eiusmod tempor incididunt ut labore et dolore magna aliqua. Quis ipsum suspendisse ultrices gravida. Risus commodo viverra maecenas accumsan lacus vel facilisis. Lorem ipsum dolor sit amet, consectetur adipiscing elit, sed do eiusmod tempor incididunt ut labore et dolore magna aliqua.</p>
      <p>Lorem ipsum dolor sit amet, consectetur adipiscing elit, sed do eiusmod tempor incididunt ut labore et dolore magna aliqua. Quis ipsum suspendisse ultrices gravida. Risus commodo viverra maecenas accumsan lacus vel facilisis.</p>
    </div>
    <div class="art about-astro" role="img" aria-label="Cartoon astronaut riding a small rocket"></div>
    <div class="planet-surface" role="img" aria-label="Cartoon planet surface with craters"></div>
  </section>

  <section class="slide slide-services">
    <div class="brand"><span class="brand-dot"></span><span class="brand-name">Signal Forge</span></div>
    <div class="art small-rocket" role="img" aria-label="Small cartoon rocket"></div>
    <h2 class="slide-heading services-heading">Our Services</h2>
    <div class="services-row">
      <div class="service" role="img" aria-label="Photo of colleagues smiling at a laptop"><div class="service-label"><strong>Lorem Ipsum</strong><span>Dolor sit</span></div></div>
      <div class="service" role="img" aria-label="Photo of an engineer at a computer workstation"><div class="service-label"><strong>Lorem Ipsum</strong><span>Dolor sit</span></div></div>
      <div class="service" role="img" aria-label="Photo of a developer reviewing code on screens"><div class="service-label"><strong>Lorem Ipsum</strong><span>Dolor sit</span></div></div>
    </div>
    <div class="art alien" role="img" aria-label="Friendly cartoon alien character"></div>
  </section>

  <section class="slide slide-charts">
    <div class="brand"><span class="brand-dot"></span><span class="brand-name">Signal Forge</span></div>
    <div class="charts-intro">
      <h2 class="slide-heading">Data Charts</h2>
      <p class="body-text">Lorem ipsum dolor sit amet, consectetur adipiscing elit, sed do eiusmod tempor incididunt ut labore et dolore magna aliqua. Quis ipsum suspendisse ultrices gravida.</p>
    </div>
    <svg class="chart" width="600" height="400" viewBox="0 0 600 400">
      <g stroke="#7BADD7" stroke-opacity=".25">
        <line x1="40" y1="20" x2="590" y2="20"/><line x1="40" y1="90" x2="590" y2="90"/>
        <line x1="40" y1="160" x2="590" y2="160"/><line x1="40" y1="230" x2="590" y2="230"/>
        <line x1="40" y1="300" x2="590" y2="300"/><line x1="40" y1="370" x2="590" y2="370"/>
      </g>
      <g font-family="Poppins,sans-serif" font-size="11" fill="#CADEEF" text-anchor="end">
        <text x="30" y="24">5</text><text x="30" y="94">4</text><text x="30" y="164">3</text>
        <text x="30" y="234">2</text><text x="30" y="304">1</text><text x="30" y="374">0</text>
      </g>
      <rect x="60" y="90" width="26" height="280" fill="#0054AA"/>
      <rect x="90" y="200" width="26" height="170" fill="#0677BA"/>
      <rect x="120" y="240" width="26" height="130" fill="#7BADD7"/>
      <rect x="195" y="200" width="26" height="170" fill="#0054AA"/>
      <rect x="225" y="50" width="26" height="320" fill="#0677BA"/>
      <rect x="255" y="230" width="26" height="140" fill="#7BADD7"/>
      <rect x="330" y="150" width="26" height="220" fill="#0054AA"/>
      <rect x="360" y="270" width="26" height="100" fill="#0677BA"/>
      <rect x="390" y="180" width="26" height="190" fill="#7BADD7"/>
      <rect x="465" y="60" width="26" height="310" fill="#0054AA"/>
      <rect x="495" y="130" width="26" height="240" fill="#0677BA"/>
      <rect x="525" y="40" width="26" height="330" fill="#CADEEF"/>
      <g font-family="Poppins,sans-serif" font-size="12" fill="#E8F1F8" text-anchor="middle">
        <text x="103" y="392">2020</text><text x="238" y="392">2021</text>
        <text x="373" y="392">2022</text><text x="508" y="392">2023</text>
      </g>
    </svg>
    <div class="chart-cards">
      <div class="chart-card"><h3>Lorem Ipsum</h3><p>Lorem ipsum dolor sit amet, consectetur adipiscing elit, sed do eiusmod tempor incididunt ut labore et dolore magna aliqua.</p></div>
      <div class="chart-card"><h3>Lorem Ipsum</h3><p>Lorem ipsum dolor sit amet, consectetur adipiscing elit, sed do eiusmod tempor incididunt ut labore et dolore magna aliqua.</p></div>
      <div class="chart-card"><h3>Lorem Ipsum</h3><p>Lorem ipsum dolor sit amet, consectetur adipiscing elit, sed do eiusmod tempor incididunt ut labore et dolore magna aliqua.</p></div>
    </div>
  </section>

  <section class="slide slide-goals">
    <div class="brand"><span class="brand-dot"></span><span class="brand-name">Signal Forge</span></div>
    <div class="art goals-astro" role="img" aria-label="Cartoon astronaut floating among small planets"></div>
    <div class="goals-copy body-text">
      <h2 class="slide-heading">Our Goals</h2>
      <p>Lorem ipsum dolor sit amet, consectetur adipiscing elit, sed do eiusmod tempor incididunt ut labore et dolore magna aliqua. Quis ipsum suspendisse ultrices gravida. Risus commodo viverra maecenas accumsan lacus vel facilisis.</p>
      <p>Lorem ipsum dolor sit amet, consectetur adipiscing elit, sed do eiusmod tempor incididunt ut labore et dolore magna aliqua. Quis ipsum suspendisse ultrices gravida. Risus commodo viverra maecenas accumsan lacus vel facilisis.</p>
      <p>Lorem ipsum dolor sit amet, consectetur adipiscing elit, sed do eiusmod tempor incididunt ut labore et dolore magna aliqua. Quis ipsum suspendisse ultrices gravida.</p>
    </div>
  </section>

</main>
</body>
</html>
```